Redesign of page from emergency manual

Please redesign this PDF to look better. Please don't include any stock photos. It must be legible. Making some words bold is probably a good idea.

Here are some things I like :

https://tarrowbooks.com.au/collections/frontpage/products/the-plk-v2-ebook

https://img-cd.vostramediafiles.com/qa-ejkwPLOTYY_SuCKbZNu411Qwgjv8YssPxEdzXN93hDkSRjLXK8WmfgbmrJW4ZZ3yUPK=w1052-h592-rw

```html
<!DOCTYPE html>
<html lang="en">
<head>
<meta charset="utf-8">
<title>Hypertension, Acute</title>
<link href="https://fonts.googleapis.com/css2?family=Poppins:wght@700;800&family=Arimo:wght@400;700&display=swap" rel="stylesheet">
<style>
  :root {
    --brand: #066aad;
    --brand-dark: #0a5e98;
    --ink: #1d1d1d;
    --rule: #dcdcdc;
    --paper: #ffffff;
  }
  * { box-sizing: border-box; margin: 0; padding: 0; }
  html, body { width: 1009px; height: 1200px; overflow: hidden; background: var(--paper); }
  body { font-family: "Arimo", Arial, sans-serif; color: var(--ink); }

  .page { position: relative; width: 1009px; height: 1200px; border: 3px solid var(--brand); }

  .masthead { position: absolute; left: 0; top: 0; width: 1003px; height: 226px; background: var(--brand); }
  .card-number { position: absolute; left: 33px; top: 26px; font: 800 44px "Poppins", sans-serif; color: #fff; }
  .title { position: absolute; left: 135px; font: 800 50px/1 "Poppins", sans-serif; color: #fff; letter-spacing: 0.5px; }
  .title-line1 { top: 58px; }
  .title-line2 { top: 120px; }
  .definition {
    position: absolute; left: 312px; top: 126px; width: 490px; height: 67px;
    background: #fff; border-radius: 34px;
    display: flex; align-items: center; justify-content: center; text-align: center;
    font: 700 15.5px/1.6 "Poppins", sans-serif; color: var(--brand); text-transform: uppercase;
  }
  .icon-slot { position: absolute; left: 839px; top: 31px; width: 133px; height: 133px; border-radius: 50%; background: #fff; }

  .first-steps { position: absolute; left: 54px; top: 291px; width: 536px; height: 195px; border: 3px solid var(--rule); border-top: none; }
  .first-steps .bar { height: 20px; background: var(--brand); margin: 0 -3px; }
  .first-steps .rail { position: absolute; top: 20px; bottom: 0; width: 3px; background: var(--rule); }
  .rail-a { left: 40px; } .rail-b { left: 68px; }
  .first-steps .marker { position: absolute; left: 20px; top: 40px; width: 10px; height: 10px; background: var(--brand); }
  .first-steps .lead { position: absolute; left: 44px; top: 38px; width: 480px; font-size: 15px; line-height: 1.2; }
  .bullets { list-style: none; }
  .bullets li { position: relative; padding-left: 14px; font-size: 15px; line-height: 1.2; }
  .bullets li::before { content: ""; position: absolute; left: 0; top: 4px; width: 10px; height: 10px; border-radius: 50%; background: var(--brand); }
  .first-steps .bullets { position: absolute; left: 103px; top: 92px; width: 410px; }
  .first-steps .bullets li + li { margin-top: 18px; }
  .sub-step { position: absolute; left: 126px; top: 166px; font-size: 15px; color: var(--brand-dark); }
  .sub-step b { color: var(--brand); }

  .bp-range { position: absolute; left: 615px; top: 291px; width: 336px; height: 195px; border-collapse: collapse; border: 3px solid var(--rule); }
  .bp-range th, .bp-range td { border: 3px solid var(--rule); text-align: center; }
  .bp-range .head th { background: var(--brand); color: #fff; font: 700 16px "Poppins", sans-serif; height: 41px; border-color: var(--brand); }
  .bp-range .cols th { font: 700 16px "Poppins", sans-serif; color: var(--brand); height: 37px; }
  .bp-range td { font-size: 15.5px; height: 38px; }

  .caution { position: absolute; left: 57px; top: 504px; width: 900px; font-size: 15px; line-height: 1.4; }
  .caution strong { font-family: "Poppins", sans-serif; color: var(--brand); font-weight: 700; }

  .drugs { position: absolute; left: 58px; top: 624px; width: 893px; border-collapse: collapse; border: 3px solid var(--brand); }
  .drugs .head th { height: 41px; background: var(--brand); }
  .drugs td { border: 3px solid var(--brand); height: 75px; vertical-align: middle; }
  .drugs .class { width: 224px; padding-left: 33px; font: 700 15.5px/1.45 "Poppins", sans-serif; color: var(--brand); }
  .drugs .agents { padding-left: 12px; }
  .drugs .bullets li { padding-left: 20px; font-size: 15.5px; line-height: 1.5; }
  .drugs .bullets li::before { top: 5px; }

  .differential { position: absolute; left: 74px; top: 984px; }
  .differential h2 { font: 700 16px "Poppins", sans-serif; color: var(--brand); padding-left: 25px; position: relative; }
  .differential h2::before { content: ""; position: absolute; left: 0; top: 5px; width: 10px; height: 10px; background: var(--brand); }
  .diff-col { position: absolute; }
  .diff-col li + li { margin-top: 14px; }
  .col-1 { left: 106px; top: 1016px; width: 220px; }
  .col-2 { left: 398px; top: 1016px; width: 230px; }
  .col-3 { left: 748px; top: 1026px; width: 200px; }
</style>
</head>
<body>
<main class="page">
  <header class="masthead">
    <div class="card-number">12</div>
    <h1 class="title title-line1">Hypertension,</h1>
    <div class="title title-line2">Acute</div>
    <div class="definition">Sustained high blood pressure refractory<br>to treating reversible causes</div>
    <div class="icon-slot" role="img" aria-label="Card icon area"></div>
  </header>

  <section class="first-steps">
    <div class="bar"></div>
    <span class="rail rail-a"></span><span class="rail rail-b"></span>
    <span class="marker"></span>
    <p class="lead">In pediatrics, hypertension is almost always treated by addressing likely causes such as light anesthesia or measurement error:</p>
    <ul class="bullets">
      <li>Ensure correct BP cuff size: cuff bladder width ~ 40% of limb circumference</li>
      <li>Ensure arterial line transducer is at level of heart</li>
    </ul>
    <p class="sub-step"><b>-</b> Consider placing arterial line if not already present</p>
  </section>

  <table class="bp-range">
    <tr class="head"><th colspan="3">Hypertensive Blood Pressure Range</th></tr>
    <tr class="cols"><th>Age (yr)</th><th>Systolic</th><th>Diastolic</th></tr>
    <tr><td>newborn</td><td>&gt;97</td><td>&gt;70</td></tr>
    <tr><td>1-3</td><td>&gt;105</td><td>&gt;61</td></tr>
    <tr><td>4-12</td><td>&gt;113</td><td>&gt;86</td></tr>
  </table>

  <p class="caution"><strong>CAUTION:</strong> Anti-hypertensive drugs are almost never needed for routine pediatric cases. These medications are used almost exclusively for specialized cardiac, neurosurgical, or endocrine (pheochromocytoma) cases. Consult an expert before use. Rule-out increased ICP.</p>

  <table class="drugs">
    <tr class="head"><th colspan="2"></th></tr>
    <tr><td class="class">Direct smooth<br>muscle relaxation</td><td class="agents"><ul class="bullets"><li>Sodium nitroprusside 0.5-10 MICROgrams/kg/min</li><li>HydrALAZINE 0.1-0.2 mg/kg (adult dose 5-10 mg)</li></ul></td></tr>
    <tr><td class="class">β-Adrenergic<br>blockade</td><td class="agents"><ul class="bullets"><li>Esmolol 100-500 MICROgrams/kg over 5 min, then 25-300 MICROgrams/kg/min</li><li>Labetalol (also a effect) 0.2-1 mg/kg q 10 min; 0.4-3 mg/kg/hour (infusion)</li></ul></td></tr>
    <tr><td class="class">Calcium channel<br>blockade</td><td class="agents"><ul class="bullets"><li>niCARdapine 0.5-5 MICROgrams/kg/min</li><li>Clevidipine 0.5-3.5 MICROgrams/kg/min</li></ul></td></tr>
    <tr><td class="class">D1-dopamine<br>agonist</td><td class="agents"><ul class="bullets"><li>Fenoldopam 0.2-0.8 MICROgrams/kg/min</li></ul></td></tr>
  </table>

  <section class="differential"><h2>Consider Differential (Partial):</h2></section>
  <ul class="bullets diff-col col-1">
    <li>Light anesthesia (consider vaporizer or infusion pump empty or malfunctioning)</li>
    <li>Hypercarbia</li>
  </ul>
  <ul class="bullets diff-col col-2">
    <li>Hypoxemia</li>
    <li>Arterial line transducer too low or BP cuff too small</li>
    <li>Withdrawal (EtOH or opioid)</li>
  </ul>
  <ul class="bullets diff-col col-3">
    <li>Thyroid Storm</li>
    <li>Pheochromocytoma</li>
    <li>Drug Error</li>
  </ul>
</main>
</body>
</html>
```